Plum Velvet Lines. No need for dangerous surgeries start waist training today!

Waist training is the celebrity secret to a slim sexy waist. You can lose 2-6 inches of your waist while waist training, so there is no need for dangerous surgeries.. All of our waist trainers and vest have three row hooks for maximum waist training results. Our Butt lifter lifts the butt to give you that curvy look you've always desired. Our vest cinches waist, flattens tummy, and cover back fat. Wear our waist trainer, or vest while working out, or under clothes. Our waist trainers and vest are undetectable underclothes so you can wear them any time with any thing. Use flyer to get 10% off. www.plumvelvetlines.example customercare@plumvelvetlines.

Target Market(s)

women

Industry/Entity Type

Training

Font styles to use
Serif
Sans Serif
Decorative
Script

Colors
6b449b
33b8a4
ffffff
e34297
33a6d7
fbee3e
a4cd39
f04a50
f37122

Requirements
Must have
• product description easy to read and understand
Nice to have
• silhouette curves
Should not have
• dullness

```html
<!DOCTYPE html>
<html lang="en">
<head>
<meta charset="utf-8">
<title>Plum Velvet Lines – Postcard</title>
<link rel="stylesheet" href="https://fonts.googleapis.com/css2?family=Great+Vibes&family=Open+Sans:wght@400;600&display=swap">
<style>
  :root {
    --plum: #6b449b;
    --teal: #33b8a4;
    --pink: #e34297;
    --white: #ffffff;
    --yellow: #fbee3e;
    --stage: #5a5a5a;
    --line: #9a9a9a;
  }
  * { margin: 0; padding: 0; box-sizing: border-box; }
  html, body { width: 764px; height: 1200px; overflow: hidden; }
  body { background: var(--stage); position: relative; font-family: "Open Sans", sans-serif; }

  .card {
    position: absolute;
    left: 71px;
    width: 622px;
    background: var(--white);
    overflow: hidden;
    box-shadow: 0 6px 18px rgba(0,0,0,.35);
  }
  .card--front { top: 46px; height: 545px; }
  .card--back  { top: 604px; height: 555px; }
  .card svg.card__art { position: absolute; inset: 0; width: 100%; height: 100%; }

  .script { font-family: "Great Vibes", cursive; font-weight: 400; position: absolute; line-height: 1; }
  .brand-title { top: 18px; right: 26px; font-size: 42px; color: var(--white); }
  .tagline { left: 28px; top: 462px; font-size: 42px; color: var(--plum); }

  .about-title { left: 22px; top: 26px; font-size: 44px; color: var(--white); }
  .about-copy {
    position: absolute;
    left: 22px; top: 84px;
    width: 248px;
    font-size: 12.5px;
    line-height: 1.5;
    color: var(--white);
  }
</style>
</head>
<body>

<section class="card card--front">
  <svg class="card__art" viewBox="0 0 622 545" aria-hidden="false">
    <defs>
      <linearGradient id="heroTone" x1="0" y1="0" x2="1" y2="0">
        <stop offset="0" stop-color="#7c5a57"/>
        <stop offset=".45" stop-color="#b79a91"/>
        <stop offset="1" stop-color="#eceaee"/>
      </linearGradient>
      <linearGradient id="seatedTone" x1="0" y1="0" x2="1" y2="1">
        <stop offset="0" stop-color="#f3ece8"/>
        <stop offset=".6" stop-color="#d9b9a6"/>
        <stop offset="1" stop-color="#f5f2f2"/>
      </linearGradient>
      <clipPath id="seatedWindow">
        <path d="M622 300 C520 296 425 360 392 545 H622 Z"/>
      </clipPath>
    </defs>

    <rect class="hero-photo" x="0" y="40" width="622" height="380" fill="url(#heroTone)"
          role="img" aria-label="Photo of a woman reclining in shapewear lingerie"/>

    <path class="top-band" d="M0 0 H622 V96 C470 62 290 44 0 82 Z" fill="var(--pink)"/>
    <path class="top-wave" d="M0 88 C290 50 470 68 622 102" fill="none" stroke="var(--teal)" stroke-width="12"/>
    <path class="top-gap" d="M0 96 C290 58 470 76 622 110" fill="none" stroke="var(--white)" stroke-width="5"/>

    <path class="bottom-band" d="M0 392 C170 370 320 398 440 340 C520 300 580 286 622 288 V545 H0 Z" fill="var(--teal)"/>
    <path class="bottom-gap" d="M0 384 C170 362 320 390 440 332 C520 292 580 278 622 280" fill="none" stroke="var(--white)" stroke-width="7"/>

    <path class="window-bg" d="M622 300 C520 296 425 360 392 545 H622 Z" fill="var(--white)"/>
    <rect class="seated-photo" x="380" y="290" width="242" height="255" fill="url(#seatedTone)" clip-path="url(#seatedWindow)"
          role="img" aria-label="Photo of a woman seated, seen from behind, wearing a waist trainer"/>
    <path class="window-frame" d="M622 300 C520 296 425 360 392 545" fill="none" stroke="var(--plum)" stroke-width="12"/>
  </svg>

  <h1 class="script brand-title">Plum Velvet Lines</h1>
  <p class="script tagline">Accentuate your Curves</p>
</section>

<section class="card card--back">
  <svg class="card__art" viewBox="0 0 622 555">
    <defs>
      <linearGradient id="productA" x1="0" y1="0" x2="0" y2="1">
        <stop offset="0" stop-color="#f4e6e4"/><stop offset="1" stop-color="#c99a8c"/>
      </linearGradient>
      <linearGradient id="productB" x1="0" y1="0" x2="0" y2="1">
        <stop offset="0" stop-color="#c9c4c8"/><stop offset="1" stop-color="#8d8489"/>
      </linearGradient>
      <radialGradient id="productC" cx=".5" cy=".5" r=".6">
        <stop offset="0" stop-color="#fff6a8"/><stop offset="1" stop-color="var(--yellow)"/>
      </radialGradient>
    </defs>

    <path class="about-panel" d="M0 0 H252 C292 150 296 360 330 555 H0 Z" fill="var(--teal)"/>
    <path class="divider-curve" d="M268 0 C308 150 312 360 346 555" fill="none" stroke="var(--plum)" stroke-width="12"/>

    <g class="product-thumbs">
      <circle cx="72" cy="468" r="54" fill="url(#productA)" stroke="var(--white)" stroke-width="5"
              role="img" aria-label="Photo of a woman wearing a white waist trainer"/>
      <circle cx="72" cy="468" r="58" fill="none" stroke="var(--plum)" stroke-width="4"/>
      <circle cx="168" cy="482" r="54" fill="url(#productB)" stroke="var(--white)" stroke-width="5"
              role="img" aria-label="Photo of a woman wearing a shaping vest"/>
      <circle cx="168" cy="482" r="58" fill="none" stroke="var(--plum)" stroke-width="4"/>
      <circle cx="272" cy="470" r="54" fill="url(#productC)" stroke="var(--white)" stroke-width="5"
              role="img" aria-label="Photo of a woman in a black body shaper"/>
      <circle cx="272" cy="470" r="58" fill="none" stroke="var(--plum)" stroke-width="4"/>
    </g>

    <rect class="stamp-box" x="548" y="120" width="54" height="58" fill="none" stroke="#333" stroke-width="2"/>
    <g class="address-lines" stroke="var(--line)" stroke-width="1.5">
      <line x1="392" y1="263" x2="604" y2="263"/>
      <line x1="392" y1="290" x2="604" y2="290"/>
      <line x1="392" y1="318" x2="604" y2="318"/>
      <line x1="392" y1="345" x2="604" y2="345"/>
    </g>
  </svg>

  <h2 class="script about-title">About Us</h2>
  <p class="about-copy">Waist training is the celebrity secret to a slim sexy waist. You can lose 2-6 inches of your waist, so there is no need for dangerous surgeries. All of our waist trainers and vests have three row hooks for maximum results. Our butt lifter gives you the curvy look you have always desired. Our vest cinches the waist, flattens the tummy and covers back fat. Wear them while working out or under clothes, any time. Use this flyer to get 10% off.</p>
</section>

</body>
</html>
```